Process Flow Chart for Real Estate Agency

We need a visual flow chart of the process of selling a home for our Real Estate Agency. This visual will be provided to all new staff to explain the process and also to potential clients to explain how detailed the process is. It needs to show each step as detailed in the attached word doc and use icons and arrows to show the direction of flow.

Target Market(s)

Staff & Potential Clients

Industry/Entity Type

Real Estate

Font styles to use
Sans Serif

Colors

Designer to choose colors to be used in the design.

Requirements
Must have
• Easy to read, lots of icons, colour coded with Agent in one colour, Admin in another (some tasks are either/or so not sure what to colour those ones.)
Nice to have
• Include one of the two attached logos

```html
<!DOCTYPE html>
<html lang="en">
<head>
<meta charset="utf-8">
<title>The Home Sale Process</title>
<link href="https://fonts.googleapis.com/css2?family=Montserrat:wght@400;500;700;800&display=swap" rel="stylesheet">
<style>
  :root{
    --agent:#1e8fd1;
    --admin:#1f4e8c;
    --shared:#7a5aa6;
    --arrow:#1e8fd1;
    --brand-orange:#f7941d;
    --ink:#1d1d1d;
    --paper:#ffffff;
    --icon-bg:#f2f6f9;
  }
  *{box-sizing:border-box;margin:0;padding:0}
  html,body{width:1200px;height:1185px;overflow:hidden;background:var(--paper)}
  body{font-family:'Montserrat',sans-serif;position:relative}
  .brand{position:absolute;top:62px;left:0;width:1200px;display:flex;justify-content:center;align-items:center;gap:12px}
  .brand-mark{width:34px;height:34px;border-radius:50%;background:var(--brand-orange)}
  .brand-name{font-weight:700;font-size:30px;color:var(--ink);letter-spacing:-.3px}
  .title{position:absolute;top:140px;left:0;width:1200px;text-align:center;font-weight:800;font-size:36px;color:var(--ink);letter-spacing:.5px}
  .step{position:absolute;width:255px}
  .step-label{font-weight:700;font-size:15px;color:var(--brand-orange);height:24px;line-height:20px}
  .step-box{height:80px;background:var(--agent);border-radius:10px;display:flex;align-items:center;padding:0 10px;gap:10px;overflow:hidden}
  .step.admin .step-box{background:var(--admin)}
  .step.shared .step-box{background:var(--shared)}
  .step-icon{flex:0 0 46px;height:46px;border-radius:8px;background:var(--icon-bg);display:flex;align-items:center;justify-content:center}
  .step-icon svg{width:28px;height:28px;fill:var(--agent)}
  .step.admin .step-icon svg{fill:var(--admin)}
  .step.shared .step-icon svg{fill:var(--shared)}
  .step-text{flex:1;color:#fff;font-size:11px;line-height:1.18;font-weight:500}
  .flow{position:absolute;top:0;left:0;width:1200px;height:1185px;pointer-events:none}
  .c1{left:40px}.c2{left:330px}.c3{left:620px}.c4{left:910px}
  .r0{top:230px}.r1{top:380px}.r2{top:530px}.r3{top:680px}.r4{top:830px}.r5{top:980px}
</style>
</head>
<body>
<svg width="0" height="0" style="position:absolute">
  <defs>
    <symbol id="i-phone" viewBox="0 0 24 24"><path d="M6.6 10.8a15 15 0 0 0 6.6 6.6l2.2-2.2a1 1 0 0 1 1-.25 11.4 11.4 0 0 0 3.6.57 1 1 0 0 1 1 1V20a1 1 0 0 1-1 1A17 17 0 0 1 3 4a1 1 0 0 1 1-1h3.5a1 1 0 0 1 1 1c0 1.25.2 2.45.57 3.57a1 1 0 0 1-.25 1z"/></symbol>
    <symbol id="i-check" viewBox="0 0 24 24"><path d="M19 3H5a2 2 0 0 0-2 2v14a2 2 0 0 0 2 2h14a2 2 0 0 0 2-2V5a2 2 0 0 0-2-2zm0 16H5V5h14zM10 17l-5-5 1.4-1.4 3.6 3.6 7.6-7.6L19 8z"/></symbol>
    <symbol id="i-contact" viewBox="0 0 24 24"><path d="M19 3H5a2 2 0 0 0-2 2v14a2 2 0 0 0 2 2h14a2 2 0 0 0 2-2V5a2 2 0 0 0-2-2zm-7 3a3 3 0 1 1 0 6 3 3 0 0 1 0-6zm6 12H6v-1c0-2 4-3.1 6-3.1s6 1.1 6 3.1z"/></symbol>
    <symbol id="i-calendar" viewBox="0 0 24 24"><path d="M19 4h-1V2h-2v2H8V2H6v2H5a2 2 0 0 0-2 2v14a2 2 0 0 0 2 2h14a2 2 0 0 0 2-2V6a2 2 0 0 0-2-2zm0 16H5V9h14z"/></symbol>
    <symbol id="i-chat" viewBox="0 0 24 24"><path d="M20 2H4a2 2 0 0 0-2 2v18l4-4h14a2 2 0 0 0 2-2V4a2 2 0 0 0-2-2zM6 9h12v2H6zm8 5H6v-2h8zm4-6H6V6h12z"/></symbol>
    <symbol id="i-chat2" viewBox="0 0 24 24"><path d="M21 6h-2v9H6v2a1 1 0 0 0 1 1h11l4 4V7a1 1 0 0 0-1-1zm-4 6V3a1 1 0 0 0-1-1H3a1 1 0 0 0-1 1v14l4-4h10a1 1 0 0 0 1-1z"/></symbol>
    <symbol id="i-doc" viewBox="0 0 24 24"><path d="M14 2H6a2 2 0 0 0-2 2v16a2 2 0 0 0 2 2h12a2 2 0 0 0 2-2V8zm-1 7V3.5L18.5 9z"/></symbol>
    <symbol id="i-doc-line" viewBox="0 0 24 24"><path d="M14 2H6a2 2 0 0 0-2 2v16a2 2 0 0 0 2 2h12a2 2 0 0 0 2-2V8zm4 18H6V4h7v5h5z"/></symbol>
    <symbol id="i-docs" viewBox="0 0 24 24"><path d="M16 1H4a2 2 0 0 0-2 2v14h2V3h12zm-1 4H8a2 2 0 0 0-2 2v14a2 2 0 0 0 2 2h11a2 2 0 0 0 2-2V11zm-1 7V6.5l5.5 5.5z"/></symbol>
    <symbol id="i-chart" viewBox="0 0 24 24"><path d="M14 2H6a2 2 0 0 0-2 2v16a2 2 0 0 0 2 2h12a2 2 0 0 0 2-2V8zM9 18H7v-5h2zm4 0h-2v-8h2zm4 0h-2v-3h2z"/></symbol>
    <symbol id="i-laptop" viewBox="0 0 24 24"><path d="M20 18a2 2 0 0 0 2-2V6a2 2 0 0 0-2-2H4a2 2 0 0 0-2 2v10a2 2 0 0 0 2 2H0v2h24v-2zM4 6h16v10H4z"/></symbol>
    <symbol id="i-support" viewBox="0 0 24 24"><path d="M20 15.5a11.4 11.4 0 0 1-3.6-.57 1 1 0 0 0-1 .25l-2.2 2.2a15 15 0 0 1-6.6-6.6l2.2-2.2a1 1 0 0 0 .25-1A11.4 11.4 0 0 1 8.5 4a1 1 0 0 0-1-1H4a1 1 0 0 0-1 1 17 17 0 0 0 17 17 1 1 0 0 0 1-1v-3.5a1 1 0 0 0-1-1zM12 3v10l3-3h6V3z"/></symbol>
    <symbol id="i-folder" viewBox="0 0 24 24"><path d="M10 4H4a2 2 0 0 0-2 2v12a2 2 0 0 0 2 2h16a2 2 0 0 0 2-2V8a2 2 0 0 0-2-2h-8z"/></symbol>
    <symbol id="i-mail" viewBox="0 0 24 24"><path d="M21.9 8.9 12 2 2.1 8.9A2 2 0 0 0 2 9.6V19a2 2 0 0 0 2 2h16a2 2 0 0 0 2-2V9.6a2 2 0 0 0-.1-.7zM12 14 4.2 9 12 4.5 19.8 9z"/></symbol>
    <symbol id="i-tree" viewBox="0 0 24 24"><path d="M3 3h8v5H3zm4 5h2v4h4v2H9v4h4v2H7zm6 2h8v5h-8zm0 7h8v5h-8z"/></symbol>
  </defs>
</svg>

<header class="brand">
  <span class="brand-mark"></span>
  <span class="brand-name">Harbourline Real Estate</span>
</header>
<h1 class="title">The Home Sale Process</h1>

<svg class="flow" viewBox="0 0 1200 1185" aria-hidden="true">
  <defs>
    <marker id="arrowhead" markerWidth="12" markerHeight="12" refX="10" refY="6" orient="auto" markerUnits="userSpaceOnUse">
      <path d="M0 0 L12 6 L0 12z" fill="#1e8fd1"/>
    </marker>
  </defs>
  <g stroke="#1e8fd1" stroke-width="3" fill="none" marker-end="url(#arrowhead)">
    <line x1="167" y1="334" x2="167" y2="402"/>
    <line x1="167" y1="484" x2="167" y2="552"/>
    <line x1="167" y1="634" x2="167" y2="702"/>
    <line x1="167" y1="784" x2="167" y2="852"/>
    <line x1="167" y1="934" x2="167" y2="1002"/>
    <line x1="457" y1="1004" x2="457" y2="936"/>
    <line x1="457" y1="854" x2="457" y2="786"/>
    <line x1="457" y1="704" x2="457" y2="636"/>
    <line x1="457" y1="554" x2="457" y2="486"/>
    <line x1="457" y1="404" x2="457" y2="336"/>
    <line x1="747" y1="334" x2="747" y2="402"/>
    <line x1="747" y1="484" x2="747" y2="552"/>
    <line x1="747" y1="634" x2="747" y2="702"/>
    <line x1="747" y1="784" x2="747" y2="852"/>
    <line x1="747" y1="934" x2="747" y2="1002"/>
    <line x1="1037" y1="1004" x2="1037" y2="936"/>
    <line x1="1037" y1="854" x2="1037" y2="786"/>
    <line x1="1037" y1="704" x2="1037" y2="636"/>
    <line x1="1037" y1="554" x2="1037" y2="486"/>
    <line x1="1037" y1="404" x2="1037" y2="336"/>
    <line x1="296" y1="1044" x2="328" y2="1044"/>
    <line x1="586" y1="294" x2="618" y2="294"/>
    <line x1="876" y1="1044" x2="908" y2="1044"/>
  </g>
</svg>

<div class="step agent c1 r0"><div class="step-label">Step 1</div><div class="step-box"><span class="step-icon"><svg><use href="#i-phone"/></svg></span><p class="step-text">Agent calls potential client to arrange a time to meet and obtain details about the property</p></div></div>
<div class="step agent c1 r1"><div class="step-label">Step 2</div><div class="step-box"><span class="step-icon"><svg><use href="#i-check"/></svg></span><p class="step-text">Agent ensures all decision makers will be present at meeting</p></div></div>
<div class="step agent c1 r2"><div class="step-label">Step 3</div><div class="step-box"><span class="step-icon"><svg><use href="#i-contact"/></svg></span><p class="step-text">Agent adds vendors contact details on phone</p></div></div>
<div class="step agent c1 r3"><div class="step-label">Step 4</div><div class="step-box"><span class="step-icon"><svg><use href="#i-calendar"/></svg></span><p class="step-text">Agent adds appointment to personal calendar</p></div></div>
<div class="step agent c1 r4"><div class="step-label">Step 5</div><div class="step-box"><span class="step-icon"><svg><use href="#i-chat"/></svg></span><p class="step-text">Agent sends SMS to potential client to thank them for the opportunity</p></div></div>
<div class="step shared c1 r5"><div class="step-label">Step 6</div><div class="step-box"><span class="step-icon"><svg><use href="#i-doc"/></svg></span><p class="step-text">Agent/Admin orders ARE from Pembury's</p></div></div>

<div class="step admin c2 r0"><div class="step-label">Step 12</div><div class="step-box"><span class="step-icon"><svg><use href="#i-laptop"/></svg></span><p class="step-text">Admin enters potential Vendor into CRM &amp; set 'Appraisal' Track</p></div></div>
<div class="step admin c2 r1"><div class="step-label">Step 11</div><div class="step-box"><span class="step-icon"><svg><use href="#i-docs"/></svg></span><p class="step-text">Admin prepares TMP with Marketing Costs Selection booklet, Service Offering Selection booklet, Sales Agency Agreement &amp; Benefits Form, ARE</p></div></div>
<div class="step shared c2 r2"><div class="step-label">Step 10</div><div class="step-box"><span class="step-icon"><svg><use href="#i-chart"/></svg></span><p class="step-text">Admin/Agent to research &amp; prints comparable Sales reports</p></div></div>
<div class="step shared c2 r3"><div class="step-label">Step 9</div><div class="step-box"><span class="step-icon"><svg><use href="#i-chat2"/></svg></span><p class="step-text">Admin/Agent delivers pre-listing kit (preferably within the hour) &amp; SMS potential vendor</p></div></div>
<div class="step admin c2 r4"><div class="step-label">Step 8</div><div class="step-box"><span class="step-icon"><svg><use href="#i-docs"/></svg></span><p class="step-text">Admin prepares pre-listing kit with questionnaire, sample brochure &amp; cover letter, property magazine, agent profile booklet</p></div></div>
<div class="step agent c2 r5"><div class="step-label">Step 7</div><div class="step-box"><span class="step-icon"><svg><use href="#i-doc-line"/></svg></span><p class="step-text">Agent completes a TMP to provide to Admin for Prelisting kit prep</p></div></div>

<div class="step agent c3 r0"><div class="step-label">Step 13</div><div class="step-box"><span class="step-icon"><svg><use href="#i-chat"/></svg></span><p class="step-text">Agent confirms appraisal on the morning of the appointment with an SMS</p></div></div>
<div class="step agent c3 r1"><div class="step-label">Step 14</div><div class="step-box"><span class="step-icon"><svg><use href="#i-check"/></svg></span><p class="step-text">Agent meets with potential Vendor and completes the appraisal</p></div></div>
<div class="step admin c3 r2"><div class="step-label">Step 15</div><div class="step-box"><span class="step-icon"><svg><use href="#i-docs"/></svg></span><p class="step-text">Admin prepares written appraisal report hand-deliver with coffee vouchers &amp;/or gift</p></div></div>
<div class="step agent c3 r3"><div class="step-label">Step 16</div><div class="step-box"><span class="step-icon"><svg><use href="#i-support"/></svg></span><p class="step-text">Agent hand-delivers report with coffee voucher or Larkfield chocolates</p></div></div>
<div class="step agent c3 r4"><div class="step-label">Step 17</div><div class="step-box"><span class="step-icon"><svg><use href="#i-chat2"/></svg></span><p class="step-text">Agent receives confirmation from vendor to proceed with listing &amp; arranges signing of Residential Sales Agency Agreement</p></div></div>
<div class="step admin c3 r5"><div class="step-label">Step 18</div><div class="step-box"><span class="step-icon"><svg><use href="#i-laptop"/></svg></span><p class="step-text">Admin checks Residential Sales Agency &amp; enters as Listing into CRM</p></div></div>

<div class="step admin c4 r0"><div class="step-label">Step 24</div><div class="step-box"><span class="step-icon"><svg><use href="#i-tree"/></svg></span><p class="step-text">Admin creates Property Folder in Network</p></div></div>
<div class="step admin c4 r1"><div class="step-label">Step 23</div><div class="step-box"><span class="step-icon"><svg><use href="#i-check"/></svg></span><p class="step-text">Admin confirms if Marketing has been paid upfront and prints/saves Tax Invoice</p></div></div>
<div class="step admin c4 r2"><div class="step-label">Step 22</div><div class="step-box"><span class="step-icon"><svg><use href="#i-laptop"/></svg></span><p class="step-text">Admin completes the marketing section of CRM</p></div></div>
<div class="step admin c4 r3"><div class="step-label">Step 21</div><div class="step-box"><span class="step-icon"><svg><use href="#i-check"/></svg></span><p class="step-text">Admin sets track (New Listing 1) as at date of signing Sales Agency &amp; removes Appraisal trail (if applicable)</p></div></div>
<div class="step admin c4 r4"><div class="step-label">Step 20</div><div class="step-box"><span class="step-icon"><svg><use href="#i-mail"/></svg></span><p class="step-text">Admin checks for Vendor email addresses &amp; if required call or SMS client to obtain</p></div></div>
<div class="step admin c4 r5"><div class="step-label">Step 19</div><div class="step-box"><span class="step-icon"><svg><use href="#i-folder"/></svg></span><p class="step-text">Admin completes the "New Listing Checklist" and prepares black folder</p></div></div>
</body>
</html>
```